Fundraising campaign to raise money to purchase a pub

We are a voluntary group campaigning to stop a pub from becoming residential flats by fighting planning proposals. We are also raising money to buy or lease the pub to re-open it as a community pub.I have attached a mock idea for a flyer.We are seeking a flyer that we can use to handout.

The purpose of the flyer is to invite people to our public meeting and to complete our pub survey.

We are looking for an A5 flyer in terms of size

Target Market(s)

Local residents, investors

Industry/Entity Type

Residential

Font styles to use
Serif
Sans Serif
Decorative
Script

Requirements
Must have
• Be eyecatching. Must have a summary of the campaign. Must also have website date and time of the public meeting. Must also promote the survey and website. Must also have contact details. Must have the survey. The date and the survey should be easily spotted.
Nice to have
• A picture of the plough
Should not have
• Clip art

```html
<!DOCTYPE html>
<html lang="en">
<head>
<meta charset="utf-8">
<title>Mayday! Save The Plough – Public Meeting Flyer</title>
<link href="https://fonts.googleapis.com/css2?family=Archivo+Black&family=Arimo:wght@400;700&display=swap" rel="stylesheet">
<style>
  :root {
    --paper: #fdf1ea;
    --alarm-red: #e3121b;
    --ink: #1c1c1c;
    --link-blue: #1d3fa8;
    --meeting-panel: #fff7d6;
    --photo-street-top: #8a7f74;
    --photo-street-bottom: #3b3430;
    --photo-bar-top: #7a4a26;
    --photo-bar-bottom: #c89a5e;
  }
  * { box-sizing: border-box; margin: 0; padding: 0; }
  html, body { width: 861px; height: 1200px; overflow: hidden; background: var(--paper); }
  .flyer {
    width: 861px; height: 1200px; position: relative;
    background: var(--paper);
    font-family: "Arimo", Arial, sans-serif;
    color: var(--ink);
    padding: 14px 34px 0;
  }
  .headline {
    font-family: "Archivo Black", "Arial Black", sans-serif;
    color: var(--alarm-red);
    font-size: 74px; line-height: 76px;
    text-align: center; letter-spacing: 1px;
  }
  .photo {
    display: block; width: 793px; margin: 0 auto;
  }
  .photo-exterior {
    height: 238px; margin-top: 10px;
    background: linear-gradient(180deg, var(--photo-street-top), var(--photo-street-bottom));
  }
  .summary { margin-top: 18px; font-size: 17.5px; line-height: 23px; }
  .summary p + p { margin-top: 12px; }
  .callout { text-align: center; font-size: 17.5px; line-height: 23px; }
  .survey { margin-top: 18px; }
  .survey-link { color: var(--link-blue); font-weight: 700; }
  .paper-copies { margin-top: 10px; }
  .web-link { font-weight: 700; color: var(--link-blue); }
  .meeting-invite { margin-top: 12px; }
  .meeting-details {
    width: 520px; margin: 8px auto 0;
    background: var(--meeting-panel);
    border: 2px solid var(--alarm-red);
    color: var(--alarm-red); font-weight: 700;
    text-align: center; font-size: 19px; line-height: 23px; padding: 3px 10px;
  }
  .photo-interior {
    height: 262px; margin-top: 14px;
    background: linear-gradient(180deg, var(--photo-bar-top), var(--photo-bar-bottom));
  }
  .contact { text-align: center; margin-top: 10px; color: var(--alarm-red); font-weight: 700; }
  .contact-intro { font-size: 19px; line-height: 24px; }
  .contact-line { font-size: 29px; line-height: 38px; }
  .contact-line .phone-lead { font-size: 19px; }
  .contact-line svg { vertical-align: -3px; margin: 0 4px; }
</style>
</head>
<body>
<main class="flyer">
  <h1 class="headline">MAYDAY! MAYDAY!</h1>

  <div class="photo photo-exterior" role="img" aria-label="Street photograph of The Plough pub frontage with its dark signboard and neighbouring shopfronts"></div>

  <section class="summary">
    <p>The Plough, 55 Elmfield Street, SE25 was purchased by a property developer, who proceeded to gut the pub and convert it into seven flats. The developer has tried twice to obtain planning permission and now is the subject of retrospective planning to put the pub back downstairs and in the basement. Should this not be forthcoming Hillbrook Council will be issue and enforcement notice to the owner.</p>
    <p>Save The Plough is a campaign to protect the building and also raise money to lease the pub or buy the building. We want to open The Plough as a community co-op pub serving great good wine.</p>
  </section>

  <section class="callout survey">
    <p>Please support our campaign by completing our survey at</p>
    <p class="survey-link">https://surveyhub.example/plough-se25-survey</p>
  </section>

  <section class="callout paper-copies">
    <p>Paper copies of the survey are available, get a friend or relative to check on</p>
    <p><span class="web-link">www.saveplough.example</span> for locations</p>
  </section>

  <section class="callout meeting-invite">
    <p>Anyone wishing to find out more about our plans to open a great pub serving fantastic food and drinks can attend our meeting on</p>
    <p class="meeting-details">18 August at 8 PM at the<br>Lantern Tavern, Linden Road, SE25</p>
  </section>

  <div class="photo photo-interior" role="img" aria-label="Panoramic photograph of the pub interior with wooden bar, seating and warm lighting"></div>

  <section class="contact">
    <p class="contact-intro">You can contact us by emailing at:</p>
    <p class="contact-line">saveploughse25@mailbox.example <span class="phone-lead">or call us at</span>
      <svg width="22" height="22" viewBox="0 0 24 24" aria-hidden="true"><circle cx="12" cy="12" r="11" fill="none" stroke="currentColor" stroke-width="2"/><path d="M8 6l2 0 1 3-1.5 1.2a7 7 0 0 0 4.3 4.3L15 13l3 1v2a2 2 0 0 1-2 2A10 10 0 0 1 6 8a2 2 0 0 1 2-2z" fill="currentColor"/></svg>2085550147</p>
  </section>
</main>
</body>
</html>
```